Multiple Packaging Solutions for LED bulbs

We need a packaging design for led bulbs for our company. We need something that can be easily adjusted in different packaging types, as we have multiple different products. It needs to be fresh, friendly, happy but at the same time corporate. We provide some basic packaging dimensions and also our logo in the respective files. The packaging could be of plastic/trasparent, or carton (regular or ecofriendly)

It Company

```html
<!DOCTYPE html>
<html lang="en">
<head>
<meta charset="utf-8">
<title>Lumora LED Packaging</title>
<link href="https://fonts.googleapis.com/css2?family=Oswald:wght@300;400;600&family=Saira+Semi+Condensed:wght@400&family=Ubuntu:wght@500&display=swap" rel="stylesheet">
<style>
  :root{
    --bg:#eeeeee;
    --white:#ffffff;
    --kraft:#dccbb0;
    --kraft-side:#cdbb9f;
    --orange:#f0a01c;
    --magenta:#e2127a;
    --ink:#2b2b2b;
    --grey:#555555;
  }
  *{margin:0;padding:0;box-sizing:border-box}
  html,body{width:1200px;height:1200px;overflow:hidden;background:var(--bg)}
  .canvas{position:relative;width:1200px;height:1200px}
  .brand{font-family:"Saira Semi Condensed",sans-serif;font-weight:400;color:var(--ink);display:flex;align-items:center;gap:12px;letter-spacing:-0.5px;white-space:nowrap}
  .brand .dot{display:inline-block;border-radius:50%;background:var(--orange)}
  .url{font-family:"Ubuntu",sans-serif;font-weight:500;color:var(--ink);position:absolute;white-space:nowrap}

  /* retail box side panel */
  .retail-side{position:absolute;left:40px;top:380px;width:200px;height:720px;background:#f4f4f4;border-right:1px solid #ddd;overflow:hidden}
  .retail-side .copy{position:absolute;left:14px;width:96px;font-family:"Oswald",sans-serif;font-weight:300;font-size:11px;line-height:17px;color:var(--grey);text-align:right}
  .retail-side .copy.intro{top:36px}
  .retail-side .copy.feel{top:330px}
  .retail-side .side-title{position:absolute;left:118px;top:270px;font-family:"Oswald",sans-serif;font-weight:300;color:var(--ink);font-size:22px;line-height:27px;white-space:nowrap}
  .retail-side .side-title .led{color:var(--magenta);font-weight:600;font-size:48px;line-height:52px;display:block}
  .retail-side .side-title small{font-size:13px;line-height:18px;display:block}
  .retail-side .deco{position:absolute;left:20px;top:470px;width:160px;height:180px;background:radial-gradient(circle at 50% 50%,#f6dca8,#f4f4f4 70%)}
  .retail-side .marks{position:absolute;left:18px;bottom:44px;display:flex;gap:6px}
  .retail-side .marks span{width:14px;height:14px;background:var(--grey);border-radius:3px}
  .retail-side .url{left:18px;bottom:16px;font-size:13px}

  /* retail box front panel */
  .retail-front{position:absolute;left:240px;top:380px;width:340px;height:720px;background:var(--white);overflow:hidden}
  .retail-front .brand{position:absolute;left:40px;top:70px;font-size:52px}
  .retail-front .brand .dot{width:26px;height:26px}
  .retail-front .accent{position:absolute;right:0;top:420px;width:130px;height:210px;background:var(--orange)}
  .retail-front .bulb{position:absolute;left:80px;top:200px;width:250px;height:420px}
  .retail-front .bulb .head{position:absolute;left:0;top:0;width:240px;height:220px;border-radius:120px 120px 60px 60px;background:linear-gradient(180deg,#f7f7f7 0%,#e6e6e6 60%,#cfd1d3 100%)}
  .retail-front .bulb .neck{position:absolute;left:95px;top:200px;width:130px;height:220px;border-radius:10px 10px 40px 40px;background:linear-gradient(180deg,#b9bcbf 0%,#9da1a4 100%)}
  .retail-front .star{position:absolute}
  .retail-front .title{position:absolute;left:36px;top:430px;font-family:"Oswald",sans-serif;font-weight:300;color:var(--ink);font-size:34px;line-height:40px;white-space:nowrap}
  .retail-front .title .led{display:block;color:var(--magenta);font-weight:600;font-size:96px;line-height:96px;letter-spacing:-2px}
  .retail-front .title small{display:block;font-size:24px;line-height:30px}
  .retail-front .specs{position:absolute;left:36px;top:645px;display:flex;gap:14px}
  .spec{background:var(--orange);color:var(--white);font-family:"Oswald",sans-serif;font-weight:600;text-align:center;border-radius:4px;padding:3px 10px;line-height:1}
  .spec b{display:block;font-size:24px}
  .spec i{font-style:normal;font-size:10px}
  .retail-front .url{left:70px;bottom:4px;font-size:17px}

  /* kraft cartons */
  .carton{position:absolute;background:var(--kraft)}
  .carton .edge{position:absolute;left:0;top:0;bottom:0;background:var(--kraft-side);display:flex;align-items:center;justify-content:center}
  .carton .edge span{transform:rotate(-90deg);font-family:"Saira Semi Condensed",sans-serif;color:var(--ink);font-size:22px;white-space:nowrap}
  .carton .deco{position:absolute;background:radial-gradient(circle at 50% 50%,rgba(240,160,28,.35),rgba(220,203,176,0) 70%)}
  .carton .certs{position:absolute;height:40px;border-radius:12px;background:var(--orange);display:flex;align-items:center;gap:8px;padding:0 14px}
  .carton .certs span{width:22px;height:24px;border:2px solid var(--ink);border-radius:2px}
  .carton .certs .rule{width:2px;height:24px;background:var(--ink);border:0}
  .carton .certs .round{border-radius:50%}

  .carton.square{left:620px;top:30px;width:540px;height:540px}
  .carton.square .edge{width:40px}
  .carton.square .brand{position:absolute;left:110px;top:110px;font-size:72px}
  .carton.square .brand .dot{width:34px;height:34px}
  .carton.square .deco{left:250px;top:210px;width:290px;height:290px}
  .carton.square .certs{left:90px;top:430px}
  .carton.square .url{right:20px;bottom:22px;font-size:26px}

  .carton.long{left:620px;top:610px;width:560px;height:300px}
  .carton.long .edge{width:40px}
  .carton.long .brand{position:absolute;left:100px;top:50px;font-size:64px}
  .carton.long .brand .dot{width:30px;height:30px}
  .carton.long .deco{left:360px;top:10px;width:200px;height:240px}
  .carton.long .certs{left:100px;top:175px}
  .carton.long .url{right:14px;bottom:22px;font-size:26px}
</style>
</head>
<body>
<main class="canvas">

  <section class="retail-side">
    <p class="copy intro">We need a packaging design for led bulbs for our company. We need something that can be easily adjusted in different packaging types, as we have corporate. We provide some basic packaging dimensions and also our logo in the respective</p>
    <p class="copy feel">Look and Feel Each slider illustrates characteristics of the customer's brand and the style your design should communicate.</p>
    <div class="side-title">LONG<br>LIFE BULB<span class="led">LED</span><small>E27 | COOL LIGHT</small></div>
    <div class="deco" role="img" aria-label="Faint orange bulb line decoration"></div>
    <div class="marks"><span></span><span></span><span></span><span></span></div>
    <div class="url">www.lumora-lights.com</div>
  </section>

  <section class="retail-front">
    <div class="brand"><span class="dot"></span>lumora</div>
    <div class="accent"></div>
    <div class="bulb" role="img" aria-label="Photo of a white LED bulb with a silver finned body and E27 screw base"><div class="head"></div><div class="neck"></div></div>
    <svg class="star" style="left:262px;top:160px" width="60" height="70" viewBox="0 0 60 70"><path d="M30 0 L36 29 L60 35 L36 41 L30 70 L24 41 L0 35 L24 29 Z" fill="var(--orange)" transform="rotate(20 30 35)"/></svg>
    <svg class="star" style="left:30px;top:380px" width="34" height="40" viewBox="0 0 60 70"><path d="M30 0 L36 29 L60 35 L36 41 L30 70 L24 41 L0 35 L24 29 Z" fill="var(--orange)"/></svg>
    <svg class="star" style="left:230px;top:630px" width="30" height="36" viewBox="0 0 60 70"><path d="M30 0 L36 29 L60 35 L36 41 L30 70 L24 41 L0 35 L24 29 Z" fill="var(--white)"/></svg>
    <div class="title">LONG<br>LIFE BULB<span class="led">LED</span><small>E27 | COOL LIGHT</small></div>
    <div class="specs">
      <div class="spec"><b>9</b><i>WATTS</i></div>
      <div class="spec"><b>700</b><i>LUMENS</i></div>
    </div>
    <div class="url">www.lumora-lights.com</div>
  </section>

  <section class="carton square">
    <div class="edge"><span>lumora</span></div>
    <div class="brand"><span class="dot"></span>lumora</div>
    <div class="deco" role="img" aria-label="Large orange bulb line decoration"></div>
    <div class="certs"><span></span><span></span><span></span><span class="rule"></span><span class="round"></span><span class="round"></span><span></span><span></span></div>
    <div class="url">www.lumora-lights.com</div>
  </section>

  <section class="carton long">
    <div class="edge"><span>lumora</span></div>
    <div class="brand"><span class="dot"></span>lumora</div>
    <div class="deco" role="img" aria-label="Large orange bulb line decoration"></div>
    <div class="certs"><span></span><span></span><span></span><span class="rule"></span><span class="round"></span><span class="round"></span><span></span><span></span></div>
    <div class="url">www.lumora-lights.com</div>
  </section>

</main>
</body>
</html>
```